Vodka Bottle Label - Selo Vodka

I need a bottle label for a vodka I'd like to make called Selo Vodka.
I would like a label that looks elegant and fresh. I would like some mountains and colours to be red and white. Open to other colours being added but not too colourful. "Selo" means fresh, dawn in polish, i would like if mountains or something extra was added to the label too. I would like the Selo Vodka name not to be too small.
The vodka is made in australia and is 37%.

I would love to have a little bit of gold colour in the label!

I will provide the back label words when completing my decision.

i'd like to make it more simple and less european looking. More australian.

I saw a bottle like this and i did like the concept.

https://www.tandemcellars.com.au/spirits/wren-vodka-range?srsltid=QxTnUwEi4kLm29-ab-c7d83efGhij_kLmNoPqRsTuVwXyz1aBcDeFgh

Target Market(s)

Vodka Drinkers

Industry/Entity Type

Alcohol

Colors
EB3D1F
EC4F4E
F09395
F8D3D4
FCEDEE

Requirements
Must have
• red and white colours incorporated, mountains or freshness on it.
Nice to have
• Fresh and clean look. Classy

```html
<!DOCTYPE html>
<html lang="en">
<head>
<meta charset="utf-8">
<title>Selo Vodka – Bottle Label</title>
<link rel="stylesheet" href="https://fonts.googleapis.com/css2?family=Antonio:wght@300;400&family=Libre+Baskerville:wght@400;700&display=swap">
<style>
  :root {
    --page: #ffffff;
    --label-red: #a11f2c;
    --brand-red: #8e1c27;
    --ring-white: #ffffff;
    --dash: #5a2a2e;
    --scene-sky: #f8f1f1;
    --scene-snow: #efdcdd;
    --scene-slope: #d9a7ab;
    --scene-base: #b45c66;
    --ribbon: #ffffff;
    --ink: #1a1416;
  }
  html, body {
    margin: 0;
    padding: 0;
    width: 1193px;
    height: 1200px;
    overflow: hidden;
    background: var(--page);
  }
  .canvas {
    position: relative;
    width: 1193px;
    height: 1200px;
    display: flex;
    align-items: center;
    justify-content: center;
  }
  .label {
    width: 1060px;
    height: 1060px;
    display: block;
  }
  .label__ring-outer { fill: var(--label-red); }
  .label__ring-gap { fill: var(--ring-white); }
  .label__ring-inner { fill: var(--label-red); }
  .label__dashes {
    fill: none;
    stroke: var(--dash);
    stroke-width: 0.8;
    stroke-dasharray: 2.2 1.6;
  }
  .brand-name {
    font-family: "Antonio", "Oswald", sans-serif;
    font-weight: 400;
    fill: var(--brand-red);
    font-size: 92px;
  }
  .ribbon__band {
    fill: var(--ribbon);
    stroke: var(--label-red);
    stroke-width: 1.4;
  }
  .ribbon__tail { fill: var(--label-red); }
  .product-type {
    font-family: "Libre Baskerville", Georgia, serif;
    font-weight: 700;
    fill: var(--ink);
    font-size: 22px;
  }
  .rim-text {
    font-family: "Libre Baskerville", Georgia, serif;
    font-weight: 400;
    fill: var(--ink);
    font-size: 7.6px;
    letter-spacing: 0.4px;
  }
</style>
</head>
<body>
<main class="canvas">
  <svg class="label" viewBox="-150 -150 300 300" xmlns="http://www.w3.org/2000/svg">
    <defs>
      <clipPath id="label-face">
        <circle r="136"/>
      </clipPath>
      <linearGradient id="mountain-tones" x1="0" y1="0" x2="0" y2="1">
        <stop offset="0" stop-color="var(--scene-sky)"/>
        <stop offset="0.3" stop-color="var(--scene-snow)"/>
        <stop offset="0.65" stop-color="var(--scene-slope)"/>
        <stop offset="1" stop-color="var(--scene-base)"/>
      </linearGradient>
      <path id="rim-left" d="M -119 -8 A 120 120 0 0 0 -84 86"/>
      <path id="rim-right" d="M 84 86 A 120 120 0 0 0 119 -8"/>
    </defs>

    <circle class="label__ring-outer" r="145"/>
    <circle class="label__ring-gap" r="140"/>
    <circle class="label__ring-inner" r="137.5"/>

    <g class="label__scene" clip-path="url(#label-face)" role="img"
       aria-label="Photograph of snow-capped mountain peaks in soft rose and white tones, with a small white snowflake emblem at the bottom centre">
      <rect x="-136" y="-136" width="272" height="272" fill="url(#mountain-tones)"/>
    </g>

    <circle class="label__dashes" r="130"/>
    <circle class="label__dashes" r="127"/>

    <text class="brand-name" x="-3" y="12" text-anchor="middle"
          textLength="186" lengthAdjust="spacing">SELO</text>

    <g class="ribbon">
      <path class="ribbon__tail" d="M -90 38 L -76 41 L -76 63 L -90 60 L -84 49 Z"/>
      <path class="ribbon__tail" d="M 86 34 L 72 36 L 72 58 L 86 56 L 80 45 Z"/>
      <path class="ribbon__band" d="M -78 43 Q -10 33 74 36 L 74 59 Q 0 55 -77 66 Z"/>
      <text class="product-type" x="-2" y="58" text-anchor="middle"
            textLength="96" lengthAdjust="spacingAndGlyphs">VODKA</text>
    </g>

    <text class="rim-text">
      <textPath href="#rim-left" startOffset="50%" text-anchor="middle">MADE IN AUSTRALIA</textPath>
    </text>
    <text class="rim-text">
      <textPath href="#rim-right" startOffset="50%" text-anchor="middle">ALC/VOL 37%</textPath>
    </text>
  </svg>
</main>
</body>
</html>
```